NovaLumaro Unique Gift Certificate

We need a unique, luxury gift certificate created for our online company (NovaLumaro). We are looking for something out of the ordinary, ie. do not want it to look like a 'normal' gift certificate. Please visit our website to gain a feel for our company (novalumaro.com.au). The dimensions are 148x148mm. We need our logo, website details, to, from, description, code, exp date included. The certificate will be printed on wood veneer so watermarks will not work. We want it to be clean and minimalistic.

Industry/Entity Type

It Company

```html
<!DOCTYPE html>
<html lang="en">
<head>
<meta charset="utf-8">
<title>NovaLumaro Gift Certificate</title>
<link rel="stylesheet" href="https://fonts.googleapis.com/css2?family=Work+Sans:wght@400;600&display=swap">
<style>
  :root {
    --veneer-light: #94603a;
    --veneer-mid: #7d4f2d;
    --veneer-dark: #5c3820;
    --ink: #ffffff;
    --badge-fill: #eef2f1;
    --badge-ring: #a9b9ba;
  }
  html, body {
    margin: 0;
    padding: 0;
    overflow: hidden;
    background: #ffffff;
  }
  .certificate {
    position: relative;
    width: 1200px;
    height: 1200px;
    overflow: hidden;
    font-family: "Work Sans", Arial, sans-serif;
    color: var(--ink);
  }
  .veneer {
    position: absolute;
    inset: 0;
    background:
      linear-gradient(90deg, rgba(60,34,18,0.18), rgba(255,220,180,0.05) 30%, rgba(60,34,18,0.15) 55%, rgba(255,220,180,0.06) 80%, rgba(60,34,18,0.2)),
      linear-gradient(180deg, var(--veneer-light), var(--veneer-mid) 55%, var(--veneer-dark));
  }
  .brand-badge {
    position: absolute;
    left: 146px;
    top: 71px;
    width: 200px;
    height: 200px;
    border-radius: 50%;
    background: var(--badge-fill);
    border: 6px solid var(--badge-ring);
    box-sizing: border-box;
  }
  .brand-name {
    position: absolute;
    left: 0;
    width: 492px;
    top: 284px;
    text-align: center;
    font-size: 30px;
    font-weight: 400;
    letter-spacing: 0.2px;
  }
  .brand-url {
    position: absolute;
    left: 53px;
    top: 347px;
    font-size: 31px;
    font-weight: 600;
    letter-spacing: 0.2px;
  }
  .guides {
    position: absolute;
    inset: 0;
    width: 1200px;
    height: 1200px;
  }
  .guide {
    fill: none;
    stroke: var(--ink);
    stroke-width: 2;
    stroke-dasharray: 2 3;
    opacity: 0.9;
  }
  .field-label {
    position: absolute;
    font-size: 23px;
    font-weight: 400;
  }
  .field-to { left: 80px; top: 597px; }
  .field-from { left: 206px; top: 665px; }
  .field-description { left: 54px; top: 791px; }
  .field-small { font-size: 16px; }
  .field-expiry { left: 91px; top: 1096px; }
  .field-code { left: 885px; top: 1105px; }
</style>
</head>
<body>
<main class="certificate">
  <div class="veneer" role="img" aria-label="Warm brown wood veneer grain texture"></div>

  <div class="brand-badge" aria-hidden="true"></div>
  <div class="brand-name">novalumaro</div>
  <div class="brand-url">novalumaro.com.au</div>

  <svg class="guides" viewBox="0 0 1050 1050" aria-hidden="true">
    <path class="guide" d="M0 578 C 300 500 560 470 655 282"/>
    <path class="guide" d="M0 650 C 450 600 950 560 930 380 Q 925 320 897 283"/>
    <path class="guide" d="M0 727 L 500 745 C 650 752 740 790 790 855"/>
  </svg>

  <div class="field-label field-to">to</div>
  <div class="field-label field-from">from</div>
  <div class="field-label field-description">description</div>
  <div class="field-label field-small field-expiry">exp date</div>
  <div class="field-label field-small field-code">code</div>
</main>
</body>
</html>
```